Velmira - New coded website

Current website is around 5 years old and corrupted in some ways...
I would like to refresh the design and to create a new coded website based on the current content .
Please refer to :
www.velmira.com.au

Coding

Coded - Design and coding required

```html
<!DOCTYPE html>
<html lang="en">
<head>
<meta charset="utf-8">
<title>Velmira – Odours Controlled Naturally</title>
<link href="https://fonts.googleapis.com/css2?family=Outfit:wght@300;400;500;600&family=Jost:ital,wght@0,400;0,500;1,400&display=swap" rel="stylesheet">
<style>
:root{
  --green:#5aa83a;
  --green-light:#7cc04f;
  --teal:#0c5872;
  --teal-dark:#0a4a61;
  --navy:#0b2535;
  --ink:#1c2a33;
  --muted:#4d5a62;
  --line:#d9e3e6;
  --white:#ffffff;
}
*{margin:0;padding:0;box-sizing:border-box}
html,body{width:1200px;height:4428px;overflow:hidden}
body{position:relative;font-family:"Jost",sans-serif;color:var(--ink);background:var(--white)}
.abs{position:absolute}
h1,h2,h3{font-family:"Outfit",sans-serif;font-weight:400}
.btn{position:absolute;display:flex;align-items:center;justify-content:center;font-family:"Outfit",sans-serif;font-size:9px;font-weight:500;letter-spacing:.6px;text-transform:uppercase}
.btn-outline{border:1.5px solid var(--green);color:var(--ink);background:#fff}
.btn-green{background:var(--green);color:#fff}
.eyebrow{font-family:"Outfit",sans-serif;font-size:12px;color:var(--green);letter-spacing:.3px}

/* header */
.topbar{left:605px;top:0;width:595px;height:32px;background:var(--navy)}
.topbar .addr{position:absolute;left:100px;top:9px;color:#fff;font-size:10px}
.quote-top{left:981px;top:0;width:144px;height:35px;background:linear-gradient(90deg,var(--green),var(--teal));color:#fff}
.brand{left:75px;top:18px;display:flex;align-items:center;gap:10px}
.brand-dot{width:56px;height:56px;border-radius:50%;background:var(--green)}
.brand-name{font-family:"Outfit",sans-serif;font-size:34px;color:var(--teal);line-height:1}
.nav{left:388px;top:54px;display:flex;font-family:"Outfit",sans-serif;font-size:10.5px}
.nav a{color:var(--ink);text-decoration:none;margin-right:36px}
.nav a.active{color:var(--green)}
.nav-divider{left:960px;top:50px;width:1px;height:26px;background:var(--line)}
.phone-top{left:985px;top:55px;font-family:"Outfit",sans-serif;font-size:12.5px;display:flex;gap:7px;align-items:center}

/* hero */
.hero{left:0;top:92px;width:1200px;height:620px;background:linear-gradient(180deg,#5d7f8e 0%,#3f6f7f 30%,#6e8c5c 60%,#4f6e3e 100%)}
.hero-copy{left:200px;top:210px;color:#fff}
.hero-copy .kicker{font-family:"Outfit",sans-serif;font-size:17px}
.hero-copy h1{font-size:46px;line-height:54px;margin-top:8px}
.hero-btn{left:200px;top:366px;width:138px;height:36px;border:1.5px solid #fff;color:#fff}
.dots{left:984px;top:248px;display:flex;flex-direction:column;gap:10px}
.dots span{width:12px;height:12px;border-radius:50%;border:1.5px solid #fff}
.dots span.on{background:radial-gradient(#fff 35%,transparent 40%)}
.hero-mark{left:564px;top:461px;width:72px;height:72px;border-radius:50%;background:#fff;border:4px solid var(--green)}

/* about */
.video{left:75px;top:663px;width:463px;height:449px;border:1.5px solid var(--green-light);background:#fff;padding:14px}
.video .art{width:100%;height:100%;background:linear-gradient(180deg,#ffffff 0%,#eef3ee 55%,#cfe2c6 80%,#f2f4f2 100%)}
.play{left:275px;top:857px;width:62px;height:62px;border-radius:50%;background:#d91c1c}
.play svg{position:absolute;left:20px;top:19px}
.about-copy{left:612px;top:732px;width:390px}
.about-copy .eyebrow{border-bottom:1.5px solid var(--green);display:inline-block;padding-bottom:9px}
.about-copy h2{font-size:29px;margin-top:26px}
.about-copy p.lead{font-size:11px;line-height:19px;margin-top:16px}
.about-copy p.small{font-size:9px;line-height:18.5px;margin-top:14px;color:var(--muted)}
.about-btn{left:612px;top:1003px;width:126px;height:35px}

/* features */
.features-bg{left:0;top:1140px;width:1200px;height:600px;background:linear-gradient(180deg,#ffffff 0%,#f3f6f6 30%,#c8d6d6 65%,#9fb4b1 100%)}
.features-title{left:0;top:1172px;width:1200px;text-align:center;font-family:"Outfit",sans-serif;font-size:17px}
.feature{top:1220px;display:flex;align-items:center;gap:12px}
.feature .ic{width:58px;height:82px;border-left:2px solid var(--ink);border-top:1.5px solid var(--ink);border-bottom:1.5px solid var(--ink);position:relative}
.feature .ic i{position:absolute;left:12px;top:20px;width:44px;height:42px;border-radius:50%;background:var(--green)}
.feature .ic i.t{background:var(--teal)}
.feature p{font-family:"Outfit",sans-serif;font-size:12px;line-height:15px}

/* products */
.products-blob{left:0;top:1420px;width:1200px;height:590px}
.products-title{left:0;top:1532px;width:1200px;text-align:center;color:#fff;font-size:28px}
.product{top:1594px;width:250px}
.product .img{height:188px;background:linear-gradient(180deg,#b9c2c6,#7c8a82 60%,#5d6b55)}
.product .cap{color:#fff;text-align:center;font-family:"Outfit",sans-serif;font-size:12px;margin-top:18px;padding-bottom:16px;border-bottom:1.5px solid rgba(255,255,255,.55)}
.discover{left:538px;top:1864px;width:124px;height:36px;border:1.5px solid #fff;color:#fff}

/* projects */
.projects-title{left:0;top:2122px;width:1200px;text-align:center;font-size:28px}
.tabs-line{left:200px;top:2218px;width:800px;height:1px;background:var(--line)}
.tab{top:2195px;height:23px;transform:skewX(-20deg);border:1px solid var(--line);border-bottom:none;background:#fff;display:flex;align-items:center;justify-content:center}
.tab span{transform:skewX(20deg);font-family:"Outfit",sans-serif;font-size:8.5px;font-weight:500;letter-spacing:.5px}
.tab.on{background:linear-gradient(90deg,var(--green),var(--teal));border:none}
.tab.on span{color:#fff}
.proj-side{top:2304px;width:306px;height:249px;background:linear-gradient(180deg,#a9bfd0,#8a9a86 60%,#b49a7c)}
.proj-main{left:406px;top:2254px;width:388px;height:349px;background:linear-gradient(180deg,#9fbfd9 0%,#5f7a64 45%,#27343a 75%,var(--teal-dark) 100%)}
.proj-cap{left:406px;top:2540px;width:388px;text-align:center;color:#fff;font-family:"Outfit",sans-serif;font-size:12px;line-height:18px}
.arrow{top:2416px;width:24px;height:24px;border-radius:50%;background:#fff;display:flex;align-items:center;justify-content:center}
.view-all{left:537px;top:2635px;width:125px;height:36px;font-size:8.5px}

/* testimonials */
.testi-bg{left:0;top:2700px;width:1200px;height:760px;background:linear-gradient(180deg,#ffffff 0%,#eef6e6 50%,#f4f9f0 80%,#ffffff 100%)}
.testi-copy{left:200px;top:2762px;width:380px}
.testi-copy h2{font-size:28px;margin-top:12px}
.quote-mark{margin-top:22px}
.testi-copy blockquote{font-size:9.5px;line-height:19px;font-style:italic;color:var(--muted);margin-top:10px}
.testi-copy .who{font-family:"Outfit",sans-serif;font-size:10px;font-weight:500;margin-top:18px}
.testi-copy .where{font-size:8.5px;color:var(--muted);margin-top:6px}
.tdots{left:200px;top:3138px;display:flex;gap:10px}
.tdots span{width:12px;height:12px;border-radius:50%;border:1.5px solid var(--green)}
.tdots span.on{background:radial-gradient(var(--green) 35%,transparent 40%)}
.testi-photo{left:664px;top:2728px;width:470px;height:466px;border-radius:50%;background:linear-gradient(180deg,#d9ebf3 0%,#b8d3df 35%,#a9b65c 60%,#6c8a2c 100%)}

/* clients */
.clients-title{left:0;top:3255px;width:1200px;text-align:center;font-size:28px}
.client{top:3313px;width:148px;height:73px;background:#fff;display:flex;align-items:center;justify-content:center;gap:8px;font-family:"Outfit",sans-serif;font-size:13px;color:var(--teal);box-shadow:0 0 0 1px #eef2ee}
.client.blue{background:#1d5da8;color:#fff}
.client i{width:14px;height:14px;border-radius:50%;background:currentColor;display:block}

/* contact */
.meadow{left:0;top:3700px;width:1200px;height:385px;background:linear-gradient(180deg,#ffffff 0%,#dde8d4 12%,#9fb79a 30%,#7c9e4a 55%,#5f8a2c 100%)}
.contact-copy{left:200px;top:3538px;width:320px}
.contact-copy h2{font-size:34px}
.contact-copy p{font-family:"Outfit",sans-serif;font-size:17px;line-height:30px;margin-top:20px}
.form{left:612px;top:3449px;width:388px;height:431px;background:linear-gradient(180deg,var(--green-light) 0%,#3f9b5a 45%,var(--teal) 100%);padding:51px 50px 0}
.field{height:36px;background:#fff;margin-bottom:14px;font-size:9.5px;color:var(--muted);padding:12px 24px}
.field.msg{height:68px}
.send{height:36px;background:var(--navy);color:#fff;display:flex;align-items:center;justify-content:center;font-family:"Outfit",sans-serif;font-size:9px;letter-spacing:.6px;margin-top:-2px}

/* footer */
.footer{left:0;top:4085px;width:1200px;height:343px;background:var(--navy);color:#fff}
.footer .brand-name{color:#fff;font-size:38px}
.f-head{font-family:"Outfit",sans-serif;font-size:11.5px;letter-spacing:.4px;text-transform:uppercase}
.f-row{display:flex;gap:12px;align-items:flex-start;font-size:10px;line-height:16px}
.f-links{font-size:9.5px;line-height:22px}
.news-input{left:818px;width:307px;height:31px;background:#fff;color:var(--muted);font-size:9px;padding:10px 16px}
.news-btn{left:818px;width:100px;height:26px;background:linear-gradient(90deg,var(--green),var(--teal));color:#fff}
.f-bottom{font-size:8.5px;color:#c8d3d8}
.social{width:28px;height:28px;border-radius:50%;border:1.5px solid var(--green)}
.social.on{background:var(--teal);border-color:var(--teal)}
</style>
</head>
<body>

<!-- header -->
<div class="abs topbar"><div class="addr">
  <svg width="8" height="10" viewBox="0 0 8 10" style="vertical-align:-1px;margin-right:4px"><path d="M4 0a4 4 0 0 0-4 4c0 3 4 6 4 6s4-3 4-6a4 4 0 0 0-4-4z" fill="#7cc04f"/></svg>
  14 Harlow Crescent, Marrindale WA 6071, Australia</div></div>
<div class="btn quote-top">Request a quote</div>

<div class="abs brand">
  <div class="brand-dot"></div>
  <div class="brand-name">Velmira</div>
</div>

<nav class="abs nav">
  <a class="active" href="#">Home</a><a href="#">About Us</a><a href="#">Products</a><a href="#">How it Works</a><a href="#">Industry</a><a href="#">Our Projects</a><a href="#">Contact Us</a>
</nav>
<div class="abs nav-divider"></div>
<div class="abs phone-top">
  <svg width="12" height="12" viewBox="0 0 24 24"><path d="M6.6 10.8a15 15 0 0 0 6.6 6.6l2.2-2.2a1 1 0 0 1 1-.25 11.4 11.4 0 0 0 3.6.57 1 1 0 0 1 1 1V20a1 1 0 0 1-1 1A17 17 0 0 1 3 4a1 1 0 0 1 1-1h3.5a1 1 0 0 1 1 1c0 1.25.2 2.45.57 3.6a1 1 0 0 1-.25 1z" fill="#5aa83a"/></svg>
  +61 (08) 5550 1234
</div>

<!-- hero -->
<div class="abs hero" role="img" aria-label="Photo of a person sitting on a grassy hillside overlooking a lake and mountains"></div>
<svg class="abs" style="left:0;top:480px" width="1200" height="240" viewBox="0 0 1200 240">
  <path d="M0 165 C160 140 330 40 520 25 C650 15 720 40 820 80 C960 135 1080 190 1200 215 L1200 240 L0 240 Z" fill="#fff"/>
</svg>
<div class="abs hero-copy">
  <div class="kicker">100% Australian Owned</div>
  <h1>Odours Controlled<br>Naturally</h1>
</div>
<div class="btn hero-btn">Request a quote</div>
<div class="abs dots"><span></span><span class="on"></span><span></span><span></span></div>
<div class="abs hero-mark"></div>

<!-- about -->
<div class="abs video"><div class="art" role="img" aria-label="Illustration of a treatment plant with tanks, buildings and trees"></div></div>
<div class="abs play"><svg width="24" height="24" viewBox="0 0 24 24"><path d="M6 3l15 9-15 9z" fill="#fff"/></svg></div>
<div class="abs about-copy">
  <div class="eyebrow">ABOUT VELMIRA</div>
  <h2>Odour control solutions</h2>
  <p class="lead">Velmira uses sustainable biotechnology to resolve odour and corrosion problems in a highly efficient, environmentally friendly and cost-effective manner.</p>
  <p class="small">Our products, the VelVent series of biofilters have been specifically engineered to overcome issues traditionally associated with biofiltration, such as bed compaction and uneven moisture levels, and our patented design achieves a removal rate of up to 99.9% per stage of treatment.</p>
</div>
<div class="btn btn-outline about-btn">Explore more</div>

<!-- features -->
<div class="abs features-bg" role="img" aria-label="Misty coastal cliffs photo fading into the page"></div>
<div class="abs features-title">What makes us the best?</div>
<div class="abs feature" style="left:200px"><div class="ic"><i></i></div><p>Biological &amp;<br>Sustainable<br>Technology</p></div>
<div class="abs feature" style="left:406px"><div class="ic"><i class="t"></i></div><p>Efficient<br>Maintenance<br>Cost</p></div>
<div class="abs feature" style="left:612px"><div class="ic"><i></i></div><p>100%<br>Australian<br>Owned</p></div>
<div class="abs feature" style="left:818px"><div class="ic"><i class="t"></i></div><p>Eco<br>Friendly</p></div>
<div class="btn btn-green" style="left:469px;top:1334px;width:124px;height:36px">Request a quote</div>
<div class="btn btn-outline" style="left:606px;top:1334px;width:125px;height:36px">Explore features</div>

<!-- products -->
<svg class="abs products-blob" viewBox="0 0 1200 590">
  <path d="M0 320 C150 250 310 80 520 25 C680 -15 820 40 960 120 C1060 180 1140 220 1200 250 L1200 395 C1050 430 900 430 760 480 C600 545 460 600 300 560 C190 530 90 470 0 420 Z" fill="#0c5872"/>
  <path d="M140 505 C280 545 420 585 560 560 C700 535 850 470 1000 440 C900 500 760 560 620 580 C460 600 300 570 140 505 Z" fill="#0a4a61"/>
</svg>
<h2 class="abs products-title">Odour control products</h2>
<div class="abs product" style="left:200px"><div class="img" role="img" aria-label="Above ground biofilter tank inside a fenced enclosure"></div><div class="cap">Above Ground: VelVent SPSV</div></div>
<div class="abs product" style="left:474px"><div class="img" role="img" aria-label="Below ground unit beneath a grassy verge and footpath"></div><div class="cap">Below Ground: VelVent MHV</div></div>
<div class="abs product" style="left:750px"><div class="img" role="img" aria-label="Green carbon treatment tanks with pipework"></div><div class="cap">Final Treatment: VelCarb</div></div>
<div class="btn discover">Discover more</div>

<!-- projects -->
<h2 class="abs projects-title">Our projects</h2>
<div class="abs tabs-line"></div>
<div class="abs tab on" style="left:362px;width:118px"><span>ALL</span></div>
<div class="abs tab" style="left:488px;width:110px"><span>INDUSTRIAL</span></div>
<div class="abs tab" style="left:606px;width:109px"><span>AGRICULTURE</span></div>
<div class="abs tab" style="left:723px;width:115px"><span>MUNICIPAL</span></div>
<div class="abs proj-side" style="left:75px" role="img" aria-label="Aerial view of rows of biofilter tanks"></div>
<div class="abs proj-side" style="left:819px" role="img" aria-label="Green treatment tanks at a construction site"></div>
<div class="abs proj-main" role="img" aria-label="Black biofilter tanks behind a fence at a pump station"></div>
<div class="abs proj-cap">3000 m3/h- H2S 300ppm- Carrow Street<br>WWPS Odour Treatment Plant</div>
<div class="abs arrow" style="left:396px"><svg width="8" height="10" viewBox="0 0 8 10"><path d="M6 1L2 5l4 4" stroke="#1c2a33" stroke-width="1.5" fill="none"/></svg></div>
<div class="abs arrow" style="left:779px"><svg width="8" height="10" viewBox="0 0 8 10"><path d="M2 1l4 4-4 4" stroke="#1c2a33" stroke-width="1.5" fill="none"/></svg></div>
<div class="btn btn-outline view-all">View all projects</div>

<!-- testimonials -->
<div class="abs testi-bg"></div>
<div class="abs testi-copy">
  <div class="eyebrow">TESTIMONIALS</div>
  <h2>Happy clients say</h2>
  <svg class="quote-mark" width="34" height="24" viewBox="0 0 34 24"><path d="M2 22c0-9 3-15 10-19l1 2c-4 3-5 6-5 9h5v8zM20 22c0-9 3-15 10-19l1 2c-4 3-5 6-5 9h5v8z" fill="none" stroke="#5aa83a" stroke-width="1.8"/></svg>
  <blockquote>"Marcus and the Velmira team promised to stop the odour from our smelly neighbour and they delivered- in spades! As soon as the system was started, the smell disappeared. The system is well designed, very professionally installed and the beauty of it is, apart from a constantly running fan, it is bacteria doing the heavy lifting, so it is very environmentally friendly. We lived with the smell for 3 three years which could be extremely frustrating and unpleasant. Now, the problem is solved and we can have BBQs again. We are happy and our neighbours have noticed the odour is gone. Thank you!"</blockquote>
  <div class="who">TOM FARRELL</div>
  <div class="where">Nearby resident to Lindel Street Wastewater Pump Station</div>
</div>
<div class="abs tdots"><span></span><span class="on"></span><span></span><span></span></div>
<svg class="abs" style="left:640px;top:2704px" width="520" height="514" viewBox="0 0 520 514">
  <path d="M150 18 A240 240 0 0 0 30 330" fill="none" stroke="#5aa83a" stroke-width="9"/>
  <path d="M380 30 A240 240 0 0 1 400 450" fill="none" stroke="#0c5872" stroke-width="9"/>
</svg>
<div class="abs testi-photo" role="img" aria-label="Photo of a family playing with arms outstretched in a grassy field"></div>

<!-- clients -->
<h2 class="abs clients-title">Our clients</h2>
<div class="abs client" style="left:200px"><i></i>Northvale Council</div>
<div class="abs client" style="left:364px">City of Sandport</div>
<div class="abs client" style="left:527px"><i></i>Aqualine</div>
<div class="abs client" style="left:689px">Riverbend Water</div>
<div class="abs client blue" style="left:851px">Harbour City</div>

<!-- contact -->
<div class="abs meadow" role="img" aria-label="Photo of a person with arms raised in a sunny meadow"></div>
<div class="abs contact-copy">
  <h2>Get in contact</h2>
  <p>If you have any queries regarding out products, please do not hesitate to contact us</p>
</div>
<form class="abs form">
  <div class="field">Name</div>
  <div class="field">Phone</div>
  <div class="field">Email ...</div>
  <div class="field msg">Message</div>
  <div class="send">SEND</div>
</form>

<!-- footer -->
<footer class="abs footer">
  <div class="abs brand" style="left:75px;top:92px">
    <div class="brand-dot" style="width:66px;height:66px"></div>
    <div class="brand-name">Velmira</div>
  </div>

  <div class="abs" style="left:381px;top:95px">
    <div class="f-head">Contact us</div>
    <div class="f-row" style="margin-top:18px;font-size:13px">
      <svg width="11" height="11" viewBox="0 0 24 24"><path d="M6.6 10.8a15 15 0 0 0 6.6 6.6l2.2-2.2a1 1 0 0 1 1-.25 11.4 11.4 0 0 0 3.6.57 1 1 0 0 1 1 1V20a1 1 0 0 1-1 1A17 17 0 0 1 3 4a1 1 0 0 1 1-1h3.5a1 1 0 0 1 1 1c0 1.25.2 2.45.57 3.6a1 1 0 0 1-.25 1z" fill="#5aa83a"/></svg>
      +61 (08) 5550 1234</div>
    <div class="f-row" style="margin-top:12px">
      <svg width="10" height="8" viewBox="0 0 10 8"><rect width="10" height="8" fill="#5aa83a"/><path d="M0 0l5 4 5-4" stroke="#0b2535" fill="none"/></svg>
      info@velmira.com.au</div>
    <div class="f-row" style="margin-top:12px">
      <svg width="8" height="10" viewBox="0 0 8 10"><path d="M4 0a4 4 0 0 0-4 4c0 3 4 6 4 6s4-3 4-6a4 4 0 0 0-4-4z" fill="#5aa83a"/></svg>
      14 Harlow Crescent, Marrindale<br>WA 6071, Australia</div>
  </div>

  <div class="abs" style="left:612px;top:95px">
    <div class="f-head">Quick links</div>
    <div class="f-links" style="margin-top:10px">Odour Control Products<br>How Biofiltration Works<br>Odour Control by Industry<br>Past Projects<br>About Us</div>
  </div>

  <div class="abs" style="left:818px;top:95px"><div class="f-head">Sign up for our newsletter</div></div>
  <div class="abs news-input" style="top:124px">Enter your email ...</div>
  <div class="btn news-btn" style="top:172px">Sign up</div>

  <div class="abs f-bottom" style="left:75px;top:283px">© 2023 <span style="color:#7cc04f">VELMIRA</span>. All Right Reserved</div>
  <div class="abs f-bottom" style="left:381px;top:283px">Privacy Policy &nbsp;&nbsp;|&nbsp;&nbsp; Sitemap &nbsp;&nbsp;|&nbsp;&nbsp; ABN: 00 000 000 000</div>
  <div class="abs social" style="left:820px;top:276px" aria-label="Social link"></div>
  <div class="abs social on" style="left:857px;top:276px" aria-label="Social link"></div>
  <div class="abs social" style="left:894px;top:276px" aria-label="Social link"></div>
</footer>

</body>
</html>
```